LBH Letterhead

I need letterhead for "lakeside birch holdings llc" ...

logo attached to project..

Company Info:
482 East Marlow Avenue, Suite 7B
Chicago, Illinois 60917
ofc 312-555-0148
facsimile 312-555-0193
www.lakesidebirchholdingsllc.example
info@lakesidebirchholdingsllc.example

I have multiple projects listed.. see below:

Business cards for lakeside birch holdings llc
letterhead "
envelopes "

Business cards for KV Commerce LLC
letterhead "
envelopes "

```html
<!DOCTYPE html>
<html lang="en">
<head>
<meta charset="utf-8">
<title>Lakeside Birch Holdings LLC – Letterhead</title>
<link href="https://fonts.googleapis.com/css2?family=Tinos:ital,wght@0,400;1,400;1,700&display=swap" rel="stylesheet">
<style>
  :root {
    --navy: #1f3f73;
    --mark-tint: #c9d3e3;
    --paper: #ffffff;
  }
  html, body {
    margin: 0;
    padding: 0;
    width: 848px;
    height: 1200px;
    overflow: hidden;
    background: var(--paper);
  }
  .letterhead {
    position: relative;
    width: 848px;
    height: 1200px;
    background: var(--paper);
  }
  .brand-mark {
    position: absolute;
    left: 160px;
    top: 26px;
    width: 124px;
    height: 124px;
    background: var(--mark-tint);
  }
  .brand-name {
    position: absolute;
    left: 35px;
    top: 152px;
    margin: 0;
    font-family: "Tinos", "Times New Roman", serif;
    font-weight: 400;
    font-style: normal;
    font-size: 28px;
    letter-spacing: 0.5px;
    line-height: 1;
    color: var(--navy);
    white-space: nowrap;
  }
  .footer {
    position: absolute;
    left: 36px;
    top: 1114px;
    font-family: "Tinos", "Times New Roman", serif;
    font-style: italic;
    font-size: 12.5px;
    line-height: 17px;
    color: var(--navy);
  }
  .footer p { margin: 0; white-space: nowrap; }
  .footer .company {
    font-weight: 700;
    text-transform: uppercase;
  }
  .footer .label { font-weight: 700; }
  .footer .sep { padding: 0 6px; }
</style>
</head>
<body>
  <main class="letterhead">
    <div class="brand-mark" role="img" aria-label="Company emblem placeholder"></div>
    <h1 class="brand-name">Lakeside Birch Holdings LLC</h1>

    <footer class="footer">
      <p class="company">Lakeside Birch Holdings LLC</p>
      <p class="address">482 East Marlow Avenue, Suite 7B, Chicago, Illinois 60917</p>
      <p class="contact">
        <span class="label">ofc</span> 312-555-0148<span class="sep">|</span><span class="label">facsimile</span> 312-555-0193<span class="sep">|</span><span class="label">url</span> www.lakesidebirchholdingsllc.example<span class="sep">|</span><span class="label">email</span> info@lakesidebirchholdingsllc.example
      </p>
    </footer>
  </main>
</body>
</html>
```